The Quiet Orchard of Copper Lanterns - 40-Week Tide Ledger

I am finishing a book that is designed to be super hands on. It steps he reader through a 90 day roadmap - as a pick up, put down action diary style piece. The foundational idea is to speak about the Quiet Orchard of Copper Lanterns. With a cost of living crisis this is designed to create action and understanding. I am looking for a cover for the ebook that will blow away the competitors in the category. I want it to be bright, attractive and leap off the lumora page - appeal to a wide audience. I have pasted in a file with the best selling books in the category so you can see what's working.

```html
<!DOCTYPE html>
<html lang="en">
<head>
<meta charset="utf-8">
<title>The Quiet Orchard of Copper Lanterns - 40-Week Tide Ledger</title>
<link rel="stylesheet" href="https://fonts.googleapis.com/css2?family=Oswald:wght@300;700&family=Permanent+Marker&family=Montserrat:wght@800&display=swap">
<style>
  :root {
    --cover-blue: #0077a2;
    --title-yellow: #fff200;
    --paper: #f1f1f1;
    --brush-red: #b2080e;
    --ink: #111111;
    --white: #ffffff;
  }
  html, body {
    margin: 0;
    padding: 0;
    width: 848px;
    height: 1200px;
    overflow: hidden;
    background: var(--cover-blue);
  }
  .cover {
    display: block;
    width: 848px;
    height: 1200px;
  }
  .cover__background { fill: var(--cover-blue); }
  .title-kicker {
    font-family: "Oswald", sans-serif;
    font-weight: 700;
    fill: var(--title-yellow);
  }
  .title-main {
    font-family: "Oswald", sans-serif;
    font-weight: 700;
    fill: var(--title-yellow);
  }
  .title-joiner {
    font-family: "Oswald", sans-serif;
    font-weight: 700;
    fill: var(--ink);
  }
  .title-brush {
    font-family: "Permanent Marker", cursive;
    fill: var(--brush-red);
  }
  .title-final {
    font-family: "Oswald", sans-serif;
    font-weight: 300;
    fill: var(--white);
  }
  .paper-strip { fill: var(--paper); }
  .footer-band { fill: var(--title-yellow); }
  .footer-label {
    font-family: "Montserrat", sans-serif;
    font-weight: 800;
    fill: var(--ink);
  }
</style>
</head>
<body>
<svg class="cover" viewBox="0 0 848 1200" xmlns="http://www.w3.org/2000/svg">
  <defs>
    <filter id="strip-shadow" x="-10%" y="-20%" width="120%" height="160%">
      <feDropShadow dx="4" dy="14" stdDeviation="12" flood-color="#000" flood-opacity="0.6"/>
    </filter>
  </defs>

  <rect class="cover__background" x="0" y="0" width="848" height="1200"/>

  <text class="title-kicker" x="419" y="298" font-size="48" text-anchor="middle" textLength="122" lengthAdjust="spacingAndGlyphs">THE QUIET</text>

  <text class="title-main" x="85" y="424" font-size="160" textLength="687" lengthAdjust="spacingAndGlyphs">ORCHARD</text>

  <text class="title-final" x="102" y="910" font-size="370" textLength="644" lengthAdjust="spacingAndGlyphs">LANTERNS</text>

  <g class="title-strip" transform="rotate(-1.6 420 540)">
    <polygon class="paper-strip" filter="url(#strip-shadow)"
      points="59,432 778,432 778,622 760,624 748,620 735,626 720,623 706,628 690,625 676,630 660,627 645,632 630,629 614,634 600,631 585,636 570,632 555,637 540,634 524,639 510,636 494,641 480,637 465,642 450,639 434,644 420,640 404,645 390,642 375,647 360,643 344,648 330,645 315,650 300,646 284,651 270,648 255,653 240,649 224,654 210,651 195,656 180,652 164,657 150,654 135,659 120,655 104,660 90,657 76,662 65,659 59,661"/>
    <text class="title-joiner" x="68" y="467" font-size="30">OF</text>
    <text class="title-brush" x="68" y="618" font-size="200" textLength="704" lengthAdjust="spacingAndGlyphs">COPPER</text>
  </g>

  <rect class="footer-band" x="0" y="1116" width="848" height="84"/>
  <text class="footer-label" x="424" y="1182" font-size="49" text-anchor="middle" textLength="778" lengthAdjust="spacingAndGlyphs">40-WEEK TIDE LEDGER</text>
</svg>
</body>
</html>
```